Velduna.com webside

I want to build a Velduna.com retail website use on Shopify, reselling three main categories: Office Supplies, Packing Supplies, and Home Consumables. I also wish the webpage has the same functions as the Corvelt home page. The page is split into three different parts with the top being a sliding screen showcasing promotion products, below it being the three categories, and finally, a moving screen showing company missions.
Target Market(s)
U.S online
Industry/Entity Type
Office Supplies, packing Supplies and Home Consumables
Coding
Coded - Design and coding required
Number of Pages Required
5+ page
Look and feel

```html
<!DOCTYPE html>
<html lang="en">
<head>
<meta charset="utf-8">
<title>Velduna.com — Home</title>
<link href="https://fonts.googleapis.com/css2?family=Poppins:ital,wght@0,300;0,400;0,500;0,600;0,700;0,800;1,300;1,400&display=swap" rel="stylesheet">
<style>
:root{
  --green:#12a589;
  --green-dark:#0e8d75;
  --navy:#2c2a5c;
  --maroon:#6a1c26;
  --orange:#f08a1c;
  --yellow:#f7c21b;
  --ink:#333;
  --muted:#777;
  --line:#e3e3e3;
  --card:#f6f6f6;
  --brown:#a05a1c;
  --footer-band:#d3ebe6;
}
*{box-sizing:border-box;margin:0;padding:0}
html,body{width:1200px;height:4202px;overflow:hidden}
body{position:relative;background:#fff;font-family:'Poppins',sans-serif;color:var(--ink)}
.abs{position:absolute}
a{color:inherit;text-decoration:none}

/* header */
.topbar{left:0;top:0;width:1200px;height:77px;background:#fff;z-index:2}
.logo{font-size:25px;font-weight:400;color:#222;letter-spacing:-.2px}
.search{left:422px;top:20px;width:355px;height:35px;border:1px solid var(--green);display:flex}
.search span{flex:1;font-size:11px;color:#aaa;padding:10px 14px}
.search button{width:66px;border:0;background:var(--green);display:flex;align-items:center;justify-content:center}
.icon-btn{width:28px;height:28px;border-radius:50%;background:#e6f4f1;display:flex;align-items:center;justify-content:center}
.navbar{left:0;top:77px;width:1200px;height:45px;background:var(--green);z-index:2}
.navbar a{position:absolute;top:14px;font-size:14px;color:#fff}

/* hero */
.hero{left:0;top:122px;width:1200px;height:432px;background:var(--maroon);overflow:hidden}
.hero h1{left:174px;top:122px;font-size:41px;font-weight:800;line-height:49px;color:#fff;letter-spacing:.5px}
.hero h1 em{font-style:normal;color:var(--yellow)}
.hero .rule{left:174px;top:228px;width:90px;height:3px;background:#fff}
.btn{background:var(--green);color:#fff;font-size:12px;display:flex;align-items:center;justify-content:center;text-transform:uppercase}
.hero .btn{left:174px;top:274px;width:141px;height:34px}
.hero-photo{left:628px;top:52px;width:456px;height:340px;border-radius:40px 40px 10px 10px;background:linear-gradient(160deg,#f1f1ef,#c9c9c6)}
.badge{left:633px;top:12px;width:80px;height:80px;border-radius:50%;background:var(--yellow);color:var(--maroon);text-align:center;font-weight:700;font-size:22px;line-height:22px;padding-top:18px}
.badge small{display:block;font-size:17px;font-weight:400}

/* section titles */
.title{left:0;width:1200px;text-align:center;font-size:36px;font-weight:600;color:var(--navy)}

/* categories */
.cat{width:274px;height:372px;background:#fff;border-radius:10px;box-shadow:0 4px 14px rgba(0,0,0,.08);overflow:hidden}
.cat .photo{height:279px}
.cat h3{position:absolute;left:19px;top:305px;font-size:17px;font-weight:500;color:#333}
.cat a{position:absolute;left:19px;top:338px;font-size:14px;color:var(--green)}

/* trending */
.tab{top:1268px;height:30px;font-size:12px;display:flex;align-items:center;justify-content:center;border:1px solid #ccc;color:#888}
.tab.on{background:var(--green);border-color:var(--green);color:#fff}
.prod{top:1353px;width:202px;height:249px;background:var(--card)}
.prod .pic{position:absolute;left:16px;top:30px;width:170px;height:150px}
.prod .stars{position:absolute;left:0;width:100%;top:210px;text-align:center;color:var(--orange);font-size:11px;letter-spacing:4px}
.prod-name{top:1621px;width:202px;text-align:center;font-size:12px;color:#333}
.prod-price{top:1650px;width:202px;text-align:center;font-size:12px;color:var(--green)}
.prod-price s{color:#999;margin-left:18px}
.arrow{width:38px;height:38px;border-radius:50%;background:#eee;display:flex;align-items:center;justify-content:center}
.dot{width:9px;height:9px;border-radius:50%;background:#ccc}
.dot.on{background:var(--green)}

/* missions */
.missions{left:0;top:1816px;width:1200px;height:463px;background:linear-gradient(180deg,#a9abab,#8f9293 55%,#b5b7b6)}
.missions h2{left:0;top:114px;width:1200px;text-align:center;font-size:34px;font-weight:500;color:#fff}
.missions p{left:306px;top:190px;width:616px;text-align:center;font-size:12.5px;line-height:21px;color:#fff}
.missions .btn{left:530px;top:316px;width:140px;height:33px}

/* promos */
.promo{top:2368px;width:419px;height:248px;overflow:hidden}
.promo .save{position:absolute;left:33px;top:53px;font-size:11px;font-weight:500;color:#222;z-index:1}
.promo h3{position:absolute;left:33px;top:73px;font-size:20px;font-weight:600;color:#222;white-space:nowrap;z-index:1}
.promo p{position:absolute;left:33px;top:113px;width:215px;font-size:12px;line-height:19px;color:#444;z-index:1}
.promo .btn{position:absolute;left:33px;top:165px;width:122px;height:34px;text-transform:none;font-size:13px;z-index:1}
.promo .pic{position:absolute}

/* testimonials */
.testi{top:2828px;width:461px;height:465px}
.testi .quote{position:absolute;left:196px;width:68px;height:50px}
.testi p{position:absolute;left:72px;top:95px;width:320px;text-align:center;font-style:italic;font-weight:300;font-size:14px;line-height:21px;color:#555}
.testi .stars{position:absolute;left:0;width:100%;top:225px;text-align:center;color:var(--yellow);font-size:20px;letter-spacing:8px}
.testi .avatar{position:absolute;left:204px;top:262px;width:54px;height:54px;border-radius:50%;background:linear-gradient(#e9ddd4,#b89a86)}
.testi h4{position:absolute;left:0;width:100%;top:326px;text-align:center;font-size:20px;font-weight:600;color:var(--brown)}
.testi small{position:absolute;left:0;width:100%;top:354px;text-align:center;font-size:14px;font-style:italic;font-weight:300;color:#888}

/* newsletter */
.news{left:0;top:3434px;width:1200px;height:155px;background:linear-gradient(90deg,#a7561a,#8e2b3c 50%,#8a1f4a)}
.news h3{left:150px;top:66px;font-size:20px;font-weight:600;color:#fff}
.news .field{left:463px;top:56px;width:391px;height:46px;background:#fff;font-size:15px;color:#bbb;padding:12px 0 0 68px}
.news .sub{left:854px;top:56px;width:171px;height:46px;background:var(--green);border:2px solid #fff;color:#fff;font-size:16px;display:flex;align-items:center;justify-content:center}

/* footer */
.foot-nav a{position:absolute;top:3660px;font-size:14px;color:var(--navy)}
.foot-rule{left:176px;top:3705px;width:846px;height:1px;background:#ccc}
.foot-h{font-size:16px;font-weight:500;color:#333}
.foot-text{font-size:12.5px;line-height:25px;color:#555}
.partner-mark{font-size:20px;font-weight:700;color:var(--navy);white-space:nowrap}
.copy{left:0;top:4140px;width:1200px;height:62px;background:var(--footer-band);text-align:center;font-size:13px;color:#666;padding-top:19px}
</style>
</head>
<body>

<!-- header -->
<header class="abs topbar">
  <div class="abs logo" style="left:174px;top:24px">Velduna.com</div>
  <div class="abs search"><span>Search for anythings</span>
    <button aria-label="Search"><svg width="16" height="16" viewBox="0 0 16 16"><circle cx="6.5" cy="6.5" r="4.8" fill="none" stroke="#fff" stroke-width="2"/><path d="M10 10l4.5 4.5" stroke="#fff" stroke-width="2"/></svg></button>
  </div>
  <div class="abs icon-btn" style="left:884px;top:22px"><svg width="12" height="12" viewBox="0 0 12 12" fill="none" stroke="var(--green)" stroke-width="1.3"><circle cx="6" cy="4" r="2.4"/><path d="M1.5 11.5c0-2.6 2-4 4.5-4s4.5 1.4 4.5 4z"/></svg></div>
  <div class="abs icon-btn" style="left:940px;top:22px"><svg width="12" height="12" viewBox="0 0 12 12" fill="none" stroke="var(--green)" stroke-width="1.3"><path d="M3 8.5V5.5a3 3 0 016 0v3l1 1H2z"/><path d="M5 11h2"/></svg></div>
  <div class="abs icon-btn" style="left:997px;top:22px"><svg width="12" height="12" viewBox="0 0 12 12" fill="none" stroke="var(--green)" stroke-width="1.3"><rect x="2" y="4.5" width="8" height="6.5" rx="1"/><path d="M4 4.5V3.5a2 2 0 014 0v1"/></svg></div>
</header>
<nav class="abs navbar">
  <svg class="abs" style="left:174px;top:14px" width="17" height="14" viewBox="0 0 17 14"><path d="M0 1h17M0 7h17M0 13h17" stroke="#fff" stroke-width="2"/></svg>
  <a style="left:381px">Home</a><a style="left:461px">Shop</a><a style="left:540px">Blog</a>
  <a style="left:614px">About</a><a style="left:700px">Contact</a><a style="left:790px">FAQ</a>
</nav>

<!-- hero -->
<section class="abs hero">
  <svg class="abs" style="left:0;top:0" width="1200" height="432" viewBox="0 0 1200 432">
    <path d="M0 300 C120 330 220 370 420 370 C640 370 820 350 1000 335 C1100 326 1160 320 1200 320 L1200 432 L0 432Z" fill="var(--orange)"/>
    <path d="M0 300 C120 330 220 370 420 370" fill="none" stroke="#fff" stroke-width="2" opacity=".6"/>
  </svg>
  <h1 class="abs">Morden <em>Funiture</em><br>Collection</h1>
  <div class="abs rule"></div>
  <a class="abs btn">Shop now</a>
  <div class="abs hero-photo" role="img" aria-label="White tufted armchair with wooden legs"></div>
  <div class="abs badge">50%<small>off</small></div>
</section>

<!-- categories -->
<h2 class="abs title" style="top:630px">Shop by Category</h2>
<div class="abs cat" style="left:174px;top:707px">
  <div class="photo" role="img" aria-label="Home office desk with monitor and shelves" style="background:linear-gradient(180deg,#ecebe7,#d8d4cc)"></div>
  <h3>Office Supplies</h3><a>Explore now →</a>
</div>
<div class="abs cat" style="left:463px;top:707px">
  <div class="photo" role="img" aria-label="Stacked cardboard packing boxes on blue background" style="background:linear-gradient(180deg,#1fb0e3 0,#2aa9db 60%,#c9a77a 100%)"></div>
  <h3>Packing Supplies</h3><a>Explore now →</a>
</div>
<div class="abs cat" style="left:751px;top:707px">
  <div class="photo" role="img" aria-label="Man relaxing in armchair with laptop by a fireplace" style="background:linear-gradient(160deg,#3e3a36,#b59574 55%,#d9c6ad)"></div>
  <h3>Home Consumables</h3><a>Explore now →</a>
</div>

<!-- trending -->
<h2 class="abs title" style="top:1194px">Trending Product</h2>
<div class="abs tab on" style="left:432px;width:106px">Featured</div>
<div class="abs tab" style="left:544px;width:108px">New Product</div>
<div class="abs tab" style="left:658px;width:108px">Top Selling</div>

<div class="abs arrow" style="left:116px;top:1489px"><svg width="16" height="10" viewBox="0 0 16 10"><path d="M15 5H2M5 1L1 5l4 4" fill="none" stroke="#888" stroke-width="1.4"/></svg></div>
<div class="abs arrow" style="left:1044px;top:1489px"><svg width="16" height="10" viewBox="0 0 16 10"><path d="M1 5h13M11 1l4 4-4 4" fill="none" stroke="#888" stroke-width="1.4"/></svg></div>

<div class="abs prod" style="left:171px;background:#fff;border:1px solid #eee">
  <span class="abs" style="left:11px;top:10px;font-size:10px;color:var(--green)">50% off</span>
  <svg class="abs" style="left:180px;top:10px" width="12" height="11" viewBox="0 0 12 11"><path d="M6 10S1 6.8 1 3.6A2.6 2.6 0 016 2.3a2.6 2.6 0 015 1.3C11 6.8 6 10 6 10z" fill="none" stroke="var(--green)"/></svg>
  <div class="pic" role="img" aria-label="Split air conditioner unit with remote" style="background:linear-gradient(#f4f4f4,#d9dcde)"></div>
  <svg class="abs" style="left:20px;top:215px" width="12" height="12" viewBox="0 0 12 12" fill="none" stroke="var(--green)"><rect x="1" y="3" width="8" height="8"/><path d="M3 1h8v8"/></svg>
  <span class="abs" style="left:65px;top:213px;font-size:11px;color:#333">Add to cart</span>
  <svg class="abs" style="left:162px;top:215px" width="14" height="10" viewBox="0 0 14 10" fill="none" stroke="var(--green)"><path d="M1 5s2.5-4 6-4 6 4 6 4-2.5 4-6 4-6-4-6-4z"/><circle cx="7" cy="5" r="1.6"/></svg>
</div>
<div class="abs prod" style="left:391px"><div class="pic" role="img" aria-label="Open laptop" style="background:linear-gradient(#f6f6f6,#dedede)"></div><div class="stars">★★★★★</div></div>
<div class="abs prod" style="left:606px"><div class="pic" role="img" aria-label="Blue quilted fabric sofa" style="background:linear-gradient(#f6f6f6,#2b5cb8 60%,#f0f0f0)"></div><div class="stars">★★★★★</div></div>
<div class="abs prod" style="left:821px"><div class="pic" role="img" aria-label="Upright bagless vacuum cleaner" style="background:linear-gradient(90deg,#f6f6f6,#2f8fd1 50%,#f6f6f6)"></div><div class="stars">★★★★★</div></div>

<div class="abs prod-name" style="left:171px">Set of air conditioner ac</div>
<div class="abs prod-name" style="left:391px">ABC.CoLaptop</div>
<div class="abs prod-name" style="left:606px">Blue quilted fabric classic sofa</div>
<div class="abs prod-name" style="left:821px">Bagless Vacuum Cleaner</div>
<div class="abs prod-price" style="left:171px">$ 2,850.00<s>$ 2,850.00</s></div>
<div class="abs prod-price" style="left:391px">$ 2,850.00<s>$ 2,850.00</s></div>
<div class="abs prod-price" style="left:606px">$ 2,850.00<s>$ 2,850.00</s></div>
<div class="abs prod-price" style="left:821px">Rs. 2,850.00<s>MRP 2,850.00</s></div>

<div class="abs dot" style="left:567px;top:1709px"></div>
<div class="abs dot on" style="left:596px;top:1709px"></div>
<div class="abs dot" style="left:624px;top:1709px"></div>

<!-- missions -->
<section class="abs missions" role="img" aria-label="Bright white office interior with staircase and pendant lamps">
  <h2 class="abs">Velduna Missions</h2>
  <p class="abs">Lorem ipsum dolor sit amet, consectetur adipiscing elit, sed do eiusmod tempor incididunt ut labore et dolore magna aliqua. Ut enim ad minim veniam, quis nostrud exercitation ullamco laboris nisi ut aliquip ex ea commodo consequat. Duis aute irure dolor in reprehenderit in voluptate velit esse cillum dolore eu fugiat nulla pariatur. Excepteur sint occaecat cupidatat non proident, sunt in culpa qui officia deserunt mollit anim id est laborum.</p>
  <a class="abs btn">Explore now</a>
</section>

<!-- promos -->
<div class="abs promo" style="left:174px;background:linear-gradient(90deg,#f6ecd4,#efd8a8)">
  <div class="pic" role="img" aria-label="Yellow modern wingback chair" style="left:278px;top:22px;width:124px;height:210px;border-radius:40px 40px 10px 10px;background:linear-gradient(160deg,#f7d21c,#e5a80d)"></div>
  <span class="save">SAVE 50% OFF</span><h3>Yellow modern chair</h3>
  <p>Lorem ipsum dolor sit amet, consectetur adipiscing elit, sed</p>
  <a class="btn">Shop Now</a>
</div>
<div class="abs promo" style="left:606px;background:linear-gradient(90deg,#cfe4f2,#e9f3f9 60%,#d6e8f3)">
  <div class="pic" role="img" aria-label="Stainless steel two-door refrigerator" style="left:282px;top:15px;width:118px;height:230px;background:linear-gradient(90deg,#8e9498,#e4e7e9 40%,#b3b8bb)"></div>
  <span class="save">SAVE 50% OFF</span><h3>Modern Refrigerator</h3>
  <p>Lorem ipsum dolor sit amet, consectetur adipiscing elit, sed</p>
  <a class="btn">Shop Now</a>
</div>

<!-- testimonials -->
<h2 class="abs title" style="top:2740px">Few Words&nbsp; From Customers</h2>

<div class="abs testi" style="left:134px">
  <svg class="abs" style="left:0;top:0" width="461" height="465" viewBox="0 0 461 465" fill="none" stroke="var(--green)" stroke-width="2">
    <path d="M412 0V170"/><path d="M412 170V360a50 50 0 01-50 50H0"/>
    <path d="M461 48H100a53 53 0 00-53 53V465"/>
  </svg>
  <svg class="quote" style="top:22px" viewBox="0 0 68 50"><path d="M4 48V30C4 14 12 5 28 2l2 7c-9 3-13 8-13 15h13v24zM38 48V30c0-16 8-25 24-28l2 7c-9 3-13 8-13 15h13v24z" fill="var(--green)"/></svg>
  <p>Lorem ipsum dolor sit amet, consectetur adipiscing elit, sed do eiusmod tempor incididunt ut labore et dolore magna aliqua. Ut enim ad minim veniam, quis nostrud exercitation ullamco laboris nisi ut aliquip ex ea commodo consequat.</p>
  <div class="stars">★★★★★</div>
  <div class="avatar" role="img" aria-label="Customer portrait"></div>
  <h4>Hena Due</h4><small>Lorem ipsum</small>
  <svg class="quote" style="top:390px" viewBox="0 0 68 50"><path d="M4 48V30C4 14 12 5 28 2l2 7c-9 3-13 8-13 15h13v24zM38 48V30c0-16 8-25 24-28l2 7c-9 3-13 8-13 15h13v24z" fill="var(--green)"/></svg>
</div>
<div class="abs testi" style="left:607px">
  <svg class="abs" style="left:0;top:0" width="461" height="465" viewBox="0 0 461 465" fill="none" stroke="var(--green)" stroke-width="2">
    <path d="M412 0V170"/><path d="M412 170V360a50 50 0 01-50 50H0"/>
    <path d="M461 48H100a53 53 0 00-53 53V465"/>
  </svg>
  <svg class="quote" style="top:22px" viewBox="0 0 68 50"><path d="M4 48V30C4 14 12 5 28 2l2 7c-9 3-13 8-13 15h13v24zM38 48V30c0-16 8-25 24-28l2 7c-9 3-13 8-13 15h13v24z" fill="var(--green)"/></svg>
  <p>Lorem ipsum dolor sit amet, consectetur adipiscing elit, sed do eiusmod tempor incididunt ut labore et dolore magna aliqua. Ut enim ad minim veniam, quis nostrud exercitation ullamco laboris nisi ut aliquip ex ea commodo consequat.</p>
  <div class="stars">★★★★★</div>
  <div class="avatar" role="img" aria-label="Customer portrait" style="background:linear-gradient(#eee,#c9c3bd)"></div>
  <h4>Jhoen Due</h4><small>Lorem ipsum</small>
  <svg class="quote" style="top:390px" viewBox="0 0 68 50"><path d="M4 48V30C4 14 12 5 28 2l2 7c-9 3-13 8-13 15h13v24zM38 48V30c0-16 8-25 24-28l2 7c-9 3-13 8-13 15h13v24z" fill="var(--green)"/></svg>
</div>

<div class="abs dot" style="left:567px;top:3307px"></div>
<div class="abs dot on" style="left:596px;top:3307px"></div>
<div class="abs dot" style="left:624px;top:3307px"></div>

<!-- newsletter -->
<section class="abs news">
  <h3 class="abs">Get Notified On Best Offers</h3>
  <div class="abs field">Enter Your Email</div>
  <a class="abs sub">SUBSCRIBE</a>
</section>

<!-- footer -->
<footer>
  <div class="abs logo" style="left:176px;top:3652px">Velduna.com</div>
  <div class="foot-nav">
    <a style="left:585px">Home</a><a style="left:663px">Shop</a><a style="left:743px">Blog</a>
    <a style="left:818px">About</a><a style="left:904px">Contact</a><a style="left:994px">FAQ</a>
  </div>
  <div class="abs foot-rule"></div>

  <h4 class="abs foot-h" style="left:176px;top:3772px">About us</h4>
  <p class="abs foot-text" style="left:176px;top:3822px;width:260px">Lorem ipsum dolor sit amet, consectetur adipiscing elit, sed do eiusmod tempor incididunt ut labore et dolore magna aliqua. Ut enim ad minim veniam, quis nostrud exercitation ullamco laboris nisi ut aliquip ex ea commodo consequat. Duis aute irure dolor in reprehenderit in</p>

  <h4 class="abs foot-h" style="left:610px;top:3772px">GET IN TOUCH</h4>
  <p class="abs foot-text" style="left:610px;top:3822px">Friendlo<br>Chirper<br>Snapgrid<br>Streamly<br>Pinboardy<br>Clipora<br>Loopit</p>

  <h4 class="abs foot-h" style="left:924px;top:3772px">HELP</h4>
  <p class="abs foot-text" style="left:920px;top:3826px">Privacy<br>Refunds<br>Shipping<br>Terms of Service<br>About<br>Contact</p>

  <span class="abs" style="left:173px;top:4066px;font-size:14px;color:#333">Shipping Partner</span>
  <div class="abs" style="left:292px;top:4036px;width:2px;height:82px;background:#333"></div>
  <span class="abs partner-mark" style="left:312px;top:4040px">Parcelo</span>
  <span class="abs partner-mark" style="left:312px;top:4076px">Swiftra</span>

  <span class="abs partner-mark" style="left:662px;top:4062px">Veltra</span>
  <span class="abs partner-mark" style="left:756px;top:4062px">Paynor</span>
  <span class="abs partner-mark" style="left:852px;top:4062px">Monicard</span>
  <span class="abs partner-mark" style="left:978px;top:4062px">Purslo</span>

  <div class="abs copy">Copyright © 2022 Velduna. All rights reserved.</div>
</footer>

</body>
</html>
```